Buchcover-Design für Fachbuch
Tolle Entwürfe und ein sehr effiziente Zusammenarbeit. Können wir nur weiterempfehlen.
Zielgruppe
Unternehmensberatung im Thema Arbeitszeit. Wir haben ein Fachbuch zum Thema Arbeitszeit und Personaleinsatzplanung für Geschäftsführer, HR Mitarbeiter, Führungskräfte, Studenten und alle geschrieben, die sich o.g. Themen näher informieren möchten
Aufgabenstellung
Folgende Textelemente sollen zu sehen sein:
Autorennamen: Dr. Reinhold Kattner, Lothar Brenning
Titel: PLAN STARK Betrieb - Dienstzeiten und Schichtorganisation fair, rentabel und marktnah einrichten
Außerdem: Unter Mitwirkung von Prof. Anton K. Ruhland
Und: mit vielen Praxisbeispielen (ggf. als eine Art Plakette)
Auf der Rückseite soll ein Klappentext und 2 Zitate zu sehen sein:
Klappentext:
Die Welt verändert sich dramatisch. Digitalisierung, Fachkräftemangel, Wertewandel und nicht zuletzt Ausnahmezustände wie die Coronakrise stellen Unternehmen vor große Herausforderungen. Wie können Unternehmen flexibel und gleichzeitig wirtschaftlich, kunden- und mitarbeiterorientiert agieren?
Reinhold Kattner und Lothar Brenning sehen eine innovative Arbeitszeitgestaltung als entscheidenden Hebel an, um Unternehmen aller Branchen in schnelllebigen Märkten flexibel aufzustellen. Die Autoren beleuchten mit vielen Beispielen aus ihrer Beratungspraxis, warum Arbeitszeitsysteme dringend modernisiert werden müssen und welche Möglichkeiten Sie bereits heute haben, Arbeitszeit innovativ zu gestalten.
Sie erfahren alles Wissenswerte über klassische Modelle, wie z.B. Schichtplan, Gleitzeit, Vertrauensarbeitszeit, Zeitkontensystem und Teilzeit, über Workforce Management (Workforce Analytics, Personalbedarfsermittlung und Forecast, Personaleinsatzplanung, Zeiterfassung) bis hin zu Lebensarbeitszeit, Gruppenarbeit, Selbstorganisation, Homeoffice und New Work. Dabei lernen Sie nicht nur die Einzelkomponenten kennen, sondern erfahren auch, wie man diese geschickt zu einer für Mitarbeiter und Unternehmen gleichermaßen vorteilhaften Arbeitszeitsystematik kombiniert. Neben diesem strategischen Wissen vermitteln Ihnen die Autoren hilfreiche Methoden zur konkreten operativen Umsetzung dieser Themen.
Zitat 1:
„Durch die Weitergabe ihrer umfassenden Erfahrungen aus der Beratung ist es den Autoren in hervorragender Weise gelu..

```html
<!DOCTYPE html>
<html lang="de">
<head>
<meta charset="utf-8">
<title>PLAN STARK Betrieb – Buchcover</title>
<link rel="stylesheet" href="https://fonts.googleapis.com/css2?family=Bebas+Neue&family=Roboto:wght@300;400&family=Open+Sans:wght@400&display=swap">
<style>
  :root{
    --navy:#003a74;
    --green:#a8b84f;
    --lavender:#8e9ec7;
    --orange:#efa90f;
    --white:#ffffff;
    --page:#ffffff;
  }
  html,body{margin:0;padding:0;overflow:hidden;background:var(--page);}
  .canvas{position:relative;width:848px;height:1200px;overflow:hidden;background:var(--page);}
  .cover{position:absolute;left:81px;top:191px;width:685px;height:887px;background:var(--white);outline:1px solid #d6d6d6;}
  .block{position:absolute;}
  .photo-team{left:0;top:0;width:228px;height:201px;background:linear-gradient(135deg,#e9edf1,#cfd6de 55%,#f3f4f5);}
  .photo-nurses{left:457px;top:0;width:228px;height:201px;background:linear-gradient(120deg,#7fa6cf,#c9d7c9 50%,#9a8fc8);}
  .photo-bakery{left:0;top:483px;width:457px;height:201px;background:linear-gradient(160deg,#d8c8ad,#ece6da 50%,#b9b3a8);}
  .photo-office{left:457px;top:684px;width:228px;height:203px;background:linear-gradient(140deg,#f4f4f4,#e2e2e4 60%,#cfcac4);}
  .authors{left:228px;top:0;width:229px;height:181px;background:var(--navy);color:var(--white);
    font-family:"Roboto",sans-serif;font-weight:400;font-size:21px;line-height:31px;
    display:flex;flex-direction:column;justify-content:center;align-items:center;text-align:center;}
  .authors-strip{left:228px;top:181px;width:229px;height:20px;background:var(--lavender);}
  .bar-green{left:0;top:201px;width:20px;height:201px;background:var(--green);}
  .bar-navy{left:0;top:402px;width:20px;height:81px;background:var(--navy);}
  .title{position:absolute;left:0;top:201px;width:685px;height:282px;}
  .coop-strip{left:457px;top:483px;width:228px;height:20px;background:var(--lavender);}
  .coop{left:457px;top:503px;width:228px;height:181px;background:var(--navy);color:var(--white);
    font-family:"Roboto",sans-serif;text-align:center;}
  .coop-label{margin-top:22px;font-size:15px;font-weight:400;}
  .coop-name{margin-top:6px;font-size:20px;font-weight:400;}
  .subtitle{left:0;top:684px;width:457px;height:203px;background:var(--green);color:var(--white);
    font-family:"Roboto",sans-serif;font-weight:300;font-size:29px;line-height:37px;
    box-sizing:border-box;padding:20px 0 0 34px;}
  .badge{position:absolute;left:390px;top:589px;width:164px;height:164px;}
</style>
</head>
<body>
<div class="canvas">
  <div class="cover">
    <div class="block photo-team" role="img" aria-label="Foto: Ärzteteam bei einer Besprechung am Laptop"></div>
    <div class="block authors"><div>Dr. Reinhold Kattner</div><div>Lothar Brenning</div></div>
    <div class="block authors-strip"></div>
    <div class="block photo-nurses" role="img" aria-label="Foto: zwei Pflegekräfte im Gespräch"></div>

    <div class="block bar-green"></div>
    <div class="block bar-navy"></div>
    <svg class="title" viewBox="0 0 685 282" aria-label="PLAN STARK Betrieb">
      <g font-family="'Bebas Neue', sans-serif">
        <text x="42" y="260" font-size="154" fill="var(--green)" textLength="287" lengthAdjust="spacingAndGlyphs" transform="translate(0,-58)">PLAN</text>
        <text x="344" y="260" font-size="154" fill="var(--navy)" textLength="307" lengthAdjust="spacingAndGlyphs" transform="translate(0,-58)">STARK</text>
        <text x="341" y="257" font-size="63" fill="var(--navy)" textLength="310" lengthAdjust="spacingAndGlyphs">BETRIEB</text>
      </g>
    </svg>

    <div class="block photo-bakery" role="img" aria-label="Foto: Mitarbeitende in einer Bäckerei an der Produktionsmaschine"></div>
    <div class="block coop-strip"></div>
    <div class="block coop">
      <div class="coop-label">Unter Mitwirkung von</div>
      <div class="coop-name">Prof. Anton K. Ruhland</div>
    </div>

    <div class="block subtitle">Dienstzeiten und Schicht-<br>organisation fair, rentabel<br>und marktnah<br>einrichten</div>
    <div class="block photo-office" role="img" aria-label="Foto: Büroangestellte am Laptop"></div>

    <svg class="badge" viewBox="0 0 164 164" aria-label="mit vielen Praxisbeispielen">
      <circle cx="82" cy="82" r="82" fill="var(--white)"/>
      <circle cx="82" cy="82" r="78" fill="var(--orange)"/>
      <g transform="rotate(-8 82 82)" fill="var(--white)" font-family="'Open Sans', sans-serif" font-size="24" text-anchor="middle">
        <text x="82" y="62">mit vielen</text>
        <text x="82" y="90">Praxis-</text>
        <text x="82" y="118">beispielen</text>
      </g>
    </svg>
  </div>
</div>
</body>
</html>
```